Designing HTML Email Creative

Hi There,
The goal of this project is to design an HTML Email Creative.
Target Market: Minority Women 25 - 45. Low Household incomes. Stay at home moms. Middle America
Subject of Email Campaign: Top 5 Reasons To Go Back to College
The goal is to make the users Buy the top 5 reasons to go back to school and then Get Matched to Online & Local Colleges.
Call to action: Get Matched to Online & Local Colleges
You can add two buttons, one above the reasons and one below. The text in the button should be: Get Matched to Online & Local Colleges Now!
Your goal is to make the call to action in the email pop out so that users know very easily where to click to visit our site.
Please find attached the copy that is to be used in the creative.
Also, the information needs to be sourced so you can create very small links in the bottom of the email.
Also, we just need the psd file for this. Does not need to be coded.
Also, you can find some successful email creative attached so you have an idea.
Updates
Please note that we have updated the word doc with the correct content.
Target Market(s)
Women 25 - 50 - Low Household Incomes - Middle America
Industry/Entity Type
School
Look and feel

```html
<!DOCTYPE html>
<html lang="en">
<head>
<meta charset="utf-8">
<title>Top 5 Reasons to Go Back to College</title>
<link rel="stylesheet" href="https://fonts.googleapis.com/css2?family=Gelasio:ital,wght@0,400;1,400;1,600&family=Open+Sans:ital,wght@0,600;0,700;1,400;1,600&display=swap">
<style>
  :root {
    --page-bg: #ffffff;
    --email-bg: #ffffff;
    --red: #e8101c;
    --red-dark: #b8000a;
    --navy: #1f4e7a;
    --band: #2f6a92;
    --body-blue: #4a9ad2;
    --tagline-blue: #1d4f85;
    --footer-bg: #e9e9e9;
    --footer-text: #2b4c74;
  }
  * { margin: 0; padding: 0; box-sizing: border-box; }
  html, body { width: 1200px; height: 900px; overflow: hidden; background: var(--page-bg); }
  .email {
    position: absolute; left: 329px; top: 5px; width: 531px; height: 885px;
    background: var(--email-bg);
    box-shadow: 2px 3px 5px rgba(0,0,0,0.45);
    overflow: hidden;
  }
  .hero {
    position: absolute; left: 0; top: 0; width: 531px; height: 283px;
    background: linear-gradient(100deg, #dfeaf2 0%, #c9dbe6 30%, #c7a98c 55%, #e3c8ad 75%, #b8a48e 100%);
  }
  .hero-copy {
    position: absolute; left: 9px; top: 27px; width: 240px;
    font-family: "Gelasio", serif; font-size: 16px; line-height: 18px; color: var(--navy);
  }
  .hero-copy strong { color: var(--red); font-weight: 600; display: block; }
  .cta {
    position: absolute; height: 27px;
    background: linear-gradient(#f0232e, var(--red-dark));
    border-radius: 4px;
    box-shadow: 3px 3px 0 #5a0d10, 0 0 3px rgba(0,0,0,0.4);
    color: #fff; font-family: "Open Sans", sans-serif; font-weight: 700; font-size: 13px;
    line-height: 27px; text-align: center; text-decoration: none; white-space: nowrap;
  }
  .cta-top { left: 98px; top: 240px; width: 330px; }
  .cta-bottom { left: 84px; top: 776px; width: 333px; }
  .title-band {
    position: absolute; left: 0; top: 283px; width: 531px; height: 49px;
    background: var(--band);
    color: #fff; font-family: "Open Sans", sans-serif; font-weight: 700; font-size: 22.5px;
    line-height: 49px; text-align: center;
  }
  .reasons {
    position: absolute; left: 15px; top: 355px; width: 510px; list-style: none;
    font-family: "Open Sans", sans-serif; font-style: italic; font-weight: 600;
    font-size: 11px; line-height: 18px; letter-spacing: 0.25px;
    color: var(--body-blue); white-space: nowrap;
  }
  .reasons li { margin-bottom: 17px; }
  .reasons .reason-title { color: var(--red); }
  .tagline {
    position: absolute; left: 0; top: 704px; width: 531px; text-align: center;
    font-family: "Gelasio", serif; font-style: italic; font-weight: 400; font-size: 19px;
    line-height: 22px; color: var(--tagline-blue); white-space: nowrap;
  }
  .explore {
    position: absolute; left: 0; top: 751px; width: 500px; text-align: center;
    font-family: "Open Sans", sans-serif; font-weight: 700; font-size: 13px; color: var(--navy);
  }
  .sources {
    position: absolute; left: 0; top: 838px; width: 531px; height: 47px;
    background: var(--footer-bg); padding: 7px 0 0 4px; list-style: none;
    font-family: "Open Sans", sans-serif; font-size: 6.5px; line-height: 12px;
    letter-spacing: 0.15px; color: var(--footer-text); white-space: nowrap;
  }
</style>
</head>
<body>
  <div class="email">
    <div class="hero" role="img" aria-label="Photo of a smiling blonde woman resting her chin on her hands against a soft light blue background"></div>
    <p class="hero-copy"><strong>Empower Yourself!</strong>Education free’s you financially and boosts your self-esteem and self-confidence.</p>
    <a class="cta cta-top" href="#">Get Matched to Online &amp; Local Colleges NOW!</a>

    <h1 class="title-band">Top 5 Reasons to Go Back to College</h1>

    <ol class="reasons">
      <li><span class="reason-title">1. Education Pays</span> - Make double the money! College grads earn nearly twice as<br>much as those with only a high school diploma. Medium weekly salary with high<br>school diploma, $652. Median weelky salary with Bachelor’s degree $1,066</li>
      <li><span class="reason-title">2. Government Grants</span> - Federal Step Grants - College is more affordable than you think.<br>Federal Step Grants of up to $5,550 are available to qualifying student. Grants are free<br>money, which does not have to be paid back. Other Federal and state grants are also<br>available, as are low cost government loans and countless scholarships.</li>
      <li><span class="reason-title">3.Lower Unemployment Rates for College Grads</span> - High school Graduates are 8.3%<br>unemployed, college graduates 4.5% unemployed.</li>
      <li><span class="reason-title">4. Make One Million More in Your Lifetime</span> - Retirement Security on average, those<br>with bachelor’s degree earn 1 million more in their lifetime than those with a high<br>school diploma.</li>
      <li><span class="reason-title">5. Be More Employable</span> - Of the 2 million plus jobs added during the recent U.S.<br>economic recovery, the majorities were for college graduates.</li>
    </ol>

    <p class="tagline">You with a College Degree? ...Oh the Doors That Will Open!</p>
    <p class="explore">Click Here to Explore The Possibilities</p>
    <a class="cta cta-bottom" href="#">Get Matched to Online &amp; Local Colleges NOW!</a>

    <ul class="sources">
      <li>1.”Education Pays, National Labor Data Office, January 28, 2013 Accessed April 21,2013 &lt; www.labordataoffice.org/emp/chart_001.htm&gt;</li>
      <li>2.”Education Pays, National Labor Data Office, January 28, 2013 Accessed April 21,2013 &lt; www.labordataoffice.org/emp/chart_001.htm&gt;</li>
      <li>3.”Education Pays, National Labor Data Office, January 28, 2013 Accessed April 21,2013 &lt; www.labordataoffice.org/emp/chart_001.htm&gt;</li>
    </ul>
  </div>
</body>
</html>
```